Homepage for a commercial software website

We are looking for a main page design for our new site to support a software product. Please see attached brief and copy for details.

Please feel free to let us know if you have any questions. We also appreciate any comments and suggestions.

Deliverables
What should be delivered:
- An image of the home page design, in PNG format. The image shall contain two variants of the design: for desktop and mobile screen sizes.
- All source files, including original graphics, markups and mock-ups.
- A complete list of copyrighted materials used in the design, including fonts and graphics, with references to their origin.

Thank you!

Target Market(s)

The initial audience for this website is primarily software developers. However, as time goes by, sales may be made to various types of companies, and the site should be attractive to executives in both the engineering and the business sides of companies.

Industry/Entity Type

Software Development

Number of Pages Required

1 page

Font styles to use
Sans Serif

Colors

Designer to choose colors to be used in the design.

Requirements
Must have
• As described in the brief.
Nice to have
Should not have
• Stock photos.

```html
<!DOCTYPE html>
<html lang="en">
<head>
<meta charset="utf-8">
<title>TraceCurrent – Fast KM32 Debug Server And Flash Programmer</title>
<link rel="stylesheet" href="https://fonts.googleapis.com/css2?family=Signika:wght@300;400;600;700&display=swap">
<style>
  :root {
    --brand-blue: #1a93d0;
    --white: #ffffff;
    --ink: #111111;
    --body-grey: #555a5e;
    --accent-red: #ee3b2f;
    --rule-blue: #1a6fb0;
    --btn-start: #22bcbf;
    --btn-end: #1560a2;
  }
  * { box-sizing: border-box; margin: 0; padding: 0; }
  html, body { width: 1142px; height: 1200px; overflow: hidden; background: var(--white); }
  body { font-family: "Signika", Arial, sans-serif; position: relative; }

  .hero-band { position: absolute; left: 0; top: 0; width: 1142px; height: 615px; }

  .brand {
    position: absolute; left: 162px; top: 74px;
    color: var(--white); font-weight: 300; font-size: 27px; letter-spacing: 2px;
  }

  .social { position: absolute; top: 5px; left: 915px; display: flex; gap: 17px; }
  .social span { width: 40px; height: 40px; border-radius: 50%; background: var(--white); display: block; }

  .main-nav { position: absolute; top: 80px; left: 0; width: 1142px; height: 30px; }
  .main-nav a {
    position: absolute; color: var(--white); text-decoration: none;
    font-size: 23px; font-weight: 400;
  }
  .main-nav svg { vertical-align: middle; margin-left: 4px; }

  .hero-title {
    position: absolute; left: 170px; top: 174px; width: 800px;
    color: var(--white); font-weight: 700; font-size: 48px; line-height: 65px;
  }
  .hero-sub {
    position: absolute; left: 170px; top: 316px; width: 930px;
    color: var(--white); font-size: 27px; font-weight: 400; white-space: nowrap;
  }
  .hero-sub strong { font-weight: 600; }

  .btn-download {
    position: absolute; left: 475px; top: 444px; width: 299px; height: 81px;
    border-radius: 10px; background: linear-gradient(90deg, var(--btn-start), var(--btn-end));
    color: var(--white); font-size: 24px; display: flex; align-items: center; justify-content: center;
    text-decoration: none;
  }
  .btn-older {
    position: absolute; left: 779px; top: 473px; width: 121px; height: 40px;
    border: 2px solid var(--white); border-radius: 6px; color: var(--white);
    font-size: 13px; display: flex; align-items: center; gap: 6px; padding-left: 8px;
    text-decoration: none;
  }

  .features-heading {
    position: absolute; left: 0; top: 656px; width: 1292px; text-align: center;
    font-size: 32px; font-weight: 400; color: var(--ink);
  }
  .features-rule { position: absolute; left: 605px; top: 707px; width: 81px; height: 2px; background: var(--rule-blue); }

  .feature { position: absolute; left: 186px; width: 890px; }
  .feature h3 { font-size: 29px; font-weight: 400; color: var(--ink); position: relative; line-height: 36px; }
  .feature h3::before {
    content: ""; position: absolute; left: -18px; top: 15px; width: 11px; height: 11px;
    border-radius: 50%; background: var(--accent-red);
  }
  .feature p { font-size: 22px; font-weight: 300; color: var(--body-grey); line-height: 39px; margin-top: 3px; }
  .feature-1 { top: 738px; }
  .feature-2 { top: 970px; }
  .feature-3 { top: 1162px; }
</style>
</head>
<body>
  <svg class="hero-band" viewBox="0 0 1142 615" aria-hidden="true">
    <polygon points="0,0 1142,0 1142,523 0,615" fill="var(--brand-blue)"/>
  </svg>

  <div class="brand">TRACECURRENT</div>

  <div class="social" aria-label="Social links">
    <span></span><span></span><span></span><span></span>
  </div>

  <nav class="main-nav">
    <a href="#" style="left:581px">Download</a>
    <a href="#" style="left:759px">Docs</a>
    <a href="#" style="left:886px">News</a>
    <a href="#" style="left:1021px">Support<svg width="22" height="12" viewBox="0 0 22 12"><polyline points="1,1 11,10 21,1" fill="none" stroke="#fff" stroke-width="2"/></svg></a>
  </nav>

  <h1 class="hero-title">Fast KM32 Debug Server And<br>Flash Programmer</h1>
  <p class="hero-sub">The intelligent and reliable inferface to your <strong>SW-Probe/V2 And XLINK 2 probes.</strong></p>

  <a class="btn-download" href="#">Download Now For Windows</a>
  <a class="btn-older" href="#">
    <svg width="22" height="22" viewBox="0 0 22 22" fill="none" stroke="#fff" stroke-width="1.8">
      <path d="M4 7 A8.5 8.5 0 1 1 2.5 11"/>
      <polyline points="1.5,5 4,7.5 6.5,5"/>
      <polyline points="11,6 11,11 14,13"/>
    </svg>
    Older Version
  </a>

  <h2 class="features-heading">What Sets Us Apart?</h2>
  <div class="features-rule"></div>

  <section class="feature feature-1">
    <h3>Improved productivity</h3>
    <p>Save your time avoiding unnecessary erase/program cycles and reduce flash wearing with intelligent flash programming . TraceCurrent communicates with debug probes directly, with no third-party libraries in the middle, ensuring reliable connection, high transfer rates and detailed diagnostics.</p>
  </section>

  <section class="feature feature-2">
    <h3>No strings attached</h3>
    <p>TraceCurrent is not locked to a single proprietary type of probes or a cloud account. Develop your code offline and work with your clients and partners using vendor-recommended and integrated probes most developers already have.</p>
  </section>

  <section class="feature feature-3">
    <h3>Ready to swing into action</h3>
  </section>
</body>
</html>
```